Redesign www.KORVADO.ch - Shopify Web-Shop - Storytelling

Redesign of existing Shopify Web-page of KOR-VADO.ch.
Please carefully review both enclosed documents. The annotated notes explain the expected design direction and priorities.

```html
<!DOCTYPE html>
<html lang="en">
<head>
<meta charset="utf-8">
<title>KOR-VADO – Handmade Scarves</title>
<link href="https://fonts.googleapis.com/css2?family=Anton&family=Poppins:ital,wght@0,400;0,500;0,600;1,400&display=swap" rel="stylesheet">
<style>
:root{
  --beige:#ede5cf;
  --beige-light:#f6f1e4;
  --dark:#45464b;
  --ink:#222326;
  --muted:#6b6b70;
  --white:#ffffff;
  --line:#d8d0ba;
  --hero:#f5f4f8;
}
*{box-sizing:border-box;margin:0;padding:0}
html,body{width:1200px;height:4566px;overflow:hidden}
body{background:var(--beige);font-family:"Poppins",sans-serif;color:var(--ink);position:relative}
.abs{position:absolute}
.display{font-family:"Anton",sans-serif;font-weight:400;color:var(--ink)}
.btn{position:absolute;background:var(--dark);color:var(--white);font:600 14px "Poppins",sans-serif;letter-spacing:.3px;display:flex;align-items:center;justify-content:center;text-transform:uppercase}
.btn-sm{font-size:12px}
.top-links{top:4px;left:553px;display:flex;gap:28px;font-size:11px;color:var(--ink)}
.header{left:16px;top:25px;width:1168px;height:76px;background:var(--dark);border-radius:6px 6px 0 0}
.brand{left:131px;top:24px;color:var(--white);font:600 20px/1 "Poppins",sans-serif;letter-spacing:-.3px}
.brand small{display:block;font-size:10px;font-weight:500;letter-spacing:0;margin-top:3px}
.search{left:512px;top:25px;width:229px;height:28px;border-bottom:1px solid #cfcfd2;display:flex;align-items:center;gap:14px;color:var(--white);font-size:10px}
.cart{left:782px;top:27px;display:flex;align-items:center;gap:8px;color:var(--white);font-size:12px}
.login{left:924px;top:19px;width:110px;height:45px;border:1px solid #cfcfd2;border-radius:3px;color:var(--white);display:flex;align-items:center;justify-content:center;gap:10px;font:600 13px "Poppins",sans-serif}
.hero{left:16px;top:101px;width:1168px;height:553px;background:linear-gradient(90deg,var(--hero) 0%,var(--hero) 52%,#e9e7ea 100%);border-radius:0 0 6px 6px;overflow:hidden}
.hero-img{position:absolute;right:0;top:0;width:560px;height:553px;background:linear-gradient(160deg,#f3f3f5 0%,#d8d6d4 45%,#c94a4a 60%,#ece8e6 75%,#8a8c86 100%)}
.nav{left:131px;top:23px;font-size:14px;font-weight:500;color:var(--ink)}
.nav span{position:absolute;white-space:nowrap}
.nav .active{border-bottom:1px solid var(--ink);padding-bottom:2px}
.hero h1{left:131px;top:135px;font-size:48px;line-height:66px;width:560px}
.hero p{left:131px;top:285px;width:480px;font-size:16px;line-height:29px}
.about-img{left:149px;top:723px;width:523px;height:394px;background:linear-gradient(120deg,#9fb1c4 0%,#d7c7b0 35%,#7a3a32 60%,#b9c6d4 100%)}
.about-card{left:627px;top:789px;width:516px;height:328px;background:linear-gradient(90deg,#faf7ef,#efe7d3)}
.about-card h2{left:44px;top:36px;font-size:34px}
.about-card p{left:44px;top:111px;width:370px;font-size:13px;line-height:24.5px;color:var(--muted)}
.section-title{left:0;width:1200px;text-align:center}
.card{position:absolute;width:287px;height:394px;background:#f7f4ec;border:1px solid #e8e1cd}
.card .ph{position:absolute;left:7px;top:7px;width:273px;height:205px}
.card .name{position:absolute;left:22px;top:232px;width:243px;text-align:center;font-size:13.5px;line-height:28px}
.card .price{position:absolute;left:0;top:300px;width:100%;text-align:center;font-weight:600;font-size:18px}
.card .add{position:absolute;left:7px;top:338px;width:273px;height:43px;border:1px solid #8a8678;font-size:12.5px;font-weight:500;display:flex;align-items:center;justify-content:center;letter-spacing:.3px}
.card.hover .add{background:var(--dark);color:var(--white);border-color:var(--dark)}
.ph-pink{background:linear-gradient(160deg,#f0eeee 0%,#7a3a2a 30%,#c9a3ad 55%,#a28590 75%,#c8b9a0 100%)}
.ph-navy{background:linear-gradient(160deg,#f0eeee 0%,#7a3a2a 30%,#2b2f4a 55%,#c8a88a 75%,#c8b9a0 100%)}
.ph-vanilla{background:linear-gradient(160deg,#f0eeee 0%,#7a3a2a 30%,#efe6d6 55%,#c4a8ae 75%,#c8b9a0 100%)}
.ph-red{background:linear-gradient(160deg,#f0eeee 0%,#b38a60 25%,#2a2224 50%,#c8283a 75%,#c81f33 100%)}
.ph-dark{background:linear-gradient(160deg,#55575d 0%,#3f4046 50%,#2f3034 100%)}
.dots{left:570px;top:2105px;display:flex;gap:6px}
.dots i{width:10px;height:10px;border:1px solid var(--ink);border-radius:50%;display:block}
.dots i.on{background:var(--ink)}
.why{left:16px;top:2200px;width:1168px;height:278px;background:var(--dark);border-radius:6px}
.why h2{left:0;top:44px;width:100%;text-align:center;color:var(--white);font-size:34px}
.feature{position:absolute;top:124px;width:200px;text-align:center;color:var(--white);font-size:13px;line-height:25px}
.feature svg{display:block;margin:0 auto 12px}
.h-mid{font-size:38px}
.body-text{font-size:13px;line-height:24.5px;color:var(--muted)}
.story-img{left:599px;top:2554px;width:452px;height:334px;background:linear-gradient(110deg,#a24e34 0%,#c87a55 35%,#3b3a3c 55%,#d59c9c 75%,#8d5640 100%)}
.testi{left:147px;top:2969px;width:904px;height:293px;background:radial-gradient(ellipse at center,#f4eedf 0%,var(--beige) 75%)}
.arrow{position:absolute;top:3101px;width:40px;height:40px;border:1px solid var(--ink);border-radius:50%;display:flex;align-items:center;justify-content:center}
.everyday-img{left:147px;top:3341px;width:452px;height:332px;background:linear-gradient(120deg,#5a4a3c 0%,#9b7a55 35%,#4a4c52 60%,#c8b49a 100%)}
.footer{left:16px;top:4002px;width:1168px;height:546px;background:var(--dark);border-radius:6px 6px 0 0;color:var(--white)}
.footer h2{left:0;top:50px;width:100%;text-align:center;color:var(--white);font-size:36px}
.footer .lead{left:131px;top:112px;font-size:13px}
.sub-form{left:354px;top:162px;width:458px;height:42px;border:1px solid #cfcfd2;border-radius:3px}
.sub-form span{position:absolute;left:20px;top:13px;font-size:10px}
.sub-form b{position:absolute;right:4px;top:4px;width:104px;height:32px;background:var(--beige);color:var(--ink);font:600 13px "Poppins",sans-serif;display:flex;align-items:center;justify-content:center;border-radius:2px}
.fcol{position:absolute;top:258px;font-size:13px;line-height:27px}
.fcol h3{font:500 17px "Poppins",sans-serif;margin-bottom:6px}
.fcol .lbl{font-size:9px;font-weight:600;line-height:14px;display:block;margin-top:4px}
.fcol .val{font-size:14px;line-height:20px;display:block}
.social{display:flex;gap:10px;margin-top:18px}
.social i{width:26px;height:26px;border-radius:50%;background:var(--white);display:block}
.copyright{left:131px;top:518px;font-size:12px}
.pay{left:810px;top:514px;display:flex;gap:4px}
.pay i{width:35px;height:20px;background:var(--white);border-radius:3px;display:block}
</style>
</head>
<body>

<div class="abs top-links"><span>All Products</span><span>Triangular Scarves</span><span>Headscarves (New)</span><span>Small Triangular Scarf</span></div>

<header class="abs header">
  <div class="abs brand">KOR-VADO<small>Swiss Handmade</small></div>
  <div class="abs search">
    <svg width="28" height="28" viewBox="0 0 28 28" fill="none" stroke="#fff" stroke-width="1.6"><circle cx="13" cy="13" r="10"/><line x1="20" y1="20" x2="26" y2="26"/></svg>
    <span>SEARCH HERE....</span>
  </div>
  <div class="abs cart">
    <svg width="36" height="30" viewBox="0 0 36 30" fill="none" stroke="#fff" stroke-width="1.5"><path d="M2 5h5l4 15h16l4-11H9"/><circle cx="13" cy="25" r="2"/><circle cx="25" cy="25" r="2"/><circle cx="30" cy="5" r="5" fill="#fff"/></svg>
    <span>MY CART</span>
  </div>
  <div class="abs login">
    <svg width="16" height="18" viewBox="0 0 16 18" fill="none" stroke="#fff" stroke-width="1.4"><circle cx="8" cy="5" r="4"/><path d="M1 17c0-4 3-6 7-6s7 2 7 6z"/></svg>LOGIN
  </div>
</header>

<section class="abs hero">
  <div class="hero-img" role="img" aria-label="Striped red and white sweater with a patterned scarf on a mannequin beside green plants"></div>
  <nav class="abs nav">
    <span class="active" style="left:0">Scarves Neckerchiefs ⌄</span>
    <span style="left:225px">Hats ⌄</span>
    <span style="left:319px">Headbands</span>
    <span style="left:449px">Children ⌄</span>
    <span style="left:571px">Coupon</span>
    <span style="left:675px">About Me</span>
    <span style="left:789px">Blog</span>
    <span style="left:865px">Email</span>
  </nav>
  <h1 class="abs display">Handmade Unique Pieces For Women With Style.</h1>
  <p class="abs">Each KOR-VADO scarf is one of a kind carefully crafted to add personality to your outfit.</p>
  <div class="btn" style="left:131px;top:381px;width:223px;height:52px">Discover Scarves</div>
</section>

<div class="abs about-img" role="img" aria-label="Smiling couple walking outdoors in winter coats and scarves"></div>
<section class="abs about-card">
  <h2 class="abs display">About Us</h2>
  <p class="abs">Fabrics have been part of my life since childhood. My grandmother and my mother created with their hands and this is exactly what I continue today. I consciously take my time for each piece</p>
  <div class="btn btn-sm" style="left:47px;top:237px;width:184px;height:43px">View New Pieces</div>
</section>

<h2 class="abs display section-title" style="top:1190px;font-size:38px">A Selection For You</h2>

<div class="card" style="left:9px;top:1273px"><div class="ph ph-pink" role="img" aria-label="Pink floral triangular scarf on a wooden mannequin head"></div><div class="name">Dreieckstuch-Kleintuch Damen Ilka, Schal Damen ...</div><div class="price">CHF $39.00</div><div class="add">ADD TO CART</div></div>
<div class="card" style="left:307px;top:1273px"><div class="ph ph-pink" role="img" aria-label="Grey and pink triangular scarf on a wooden mannequin head"></div><div class="name">Dreieckstuch-Kleintuch Damen Norina, Schal Damen ...</div><div class="price">CHF $39.00</div><div class="add">ADD TO CART</div></div>
<div class="card hover" style="left:606px;top:1273px"><div class="ph ph-dark" role="img" aria-label="Dark triangular scarf on a mannequin, shown with a dimmed overlay"><svg style="position:absolute;left:117px;top:82px" width="40" height="40" viewBox="0 0 40 40"><circle cx="20" cy="20" r="19" fill="#f3ede0"/><path d="M20 11v18M11 20h18" stroke="#45464b" stroke-width="1.5"/></svg></div><div class="name">Tamsin women's triangular scarf small scarf, women's shawl ...</div><div class="price">CHF $39.00</div><div class="add">ADD TO CART</div></div>
<div class="card" style="left:904px;top:1273px"><div class="ph ph-navy" role="img" aria-label="Navy floral triangular scarf on a wooden mannequin head"></div><div class="name">Triangular scarf - small scarf for women Marla, women's ...</div><div class="price">CHF $39.00</div><div class="add">ADD TO CART</div></div>

<div class="card" style="left:9px;top:1680px"><div class="ph ph-vanilla" role="img" aria-label="Vanilla and pink triangular scarf on a wooden mannequin head"></div><div class="name">Verena triangular scarf/small scarf, pink, vanilla, turquoise ...</div><div class="price">CHF $39.00</div><div class="add">ADD TO CART</div></div>
<div class="card" style="left:307px;top:1680px"><div class="ph ph-red" role="img" aria-label="Black and pink bandana scarf on a red mannequin"></div><div class="name">Small triangular scarf, bandana</div><div class="price">CHF $39.00</div><div class="add">ADD TO CART</div></div>
<div class="card" style="left:606px;top:1680px"><div class="ph ph-pink" role="img" aria-label="Pink floral triangular scarf on a wooden mannequin head"></div><div class="name">Ilka women's triangular scarf small scarf, women's shawl ...</div><div class="price">CHF $39.00</div><div class="add">ADD TO CART</div></div>
<div class="card" style="left:904px;top:1680px"><div class="ph ph-pink" role="img" aria-label="Grey and pink triangular scarf on a wooden mannequin head"></div><div class="name">Norina triangular scarf/small scarf for women, women's scarf ...</div><div class="price">CHF $39.00</div><div class="add">ADD TO CART</div></div>

<div class="abs dots"><i></i><i class="on"></i><i></i><i></i></div>

<section class="abs why">
  <h2 class="abs display">Why KOR-VADO</h2>
  <div class="feature" style="left:98px"><svg width="38" height="38" viewBox="0 0 38 38" fill="none" stroke="#fff" stroke-width="1.3"><circle cx="19" cy="16" r="11"/><circle cx="19" cy="16" r="6"/><path d="M12 25l-3 10 5-3 3 4 2-7M26 25l3 10-5-3-3 4-2-7"/></svg>High-quality fabrics<br>without scratching</div>
  <div class="feature" style="left:342px"><svg width="38" height="38" viewBox="0 0 38 38" fill="none" stroke="#fff" stroke-width="1.3"><path d="M8 4l24 26M30 4L6 30"/><circle cx="8" cy="32" r="4"/><circle cx="30" cy="32" r="4"/></svg>Only 1–3 pieces<br>per design</div>
  <div class="feature" style="left:602px"><svg width="38" height="38" viewBox="0 0 38 38" fill="none" stroke="#fff" stroke-width="1.3"><path d="M4 14l18-8 12 6-18 8z"/><path d="M4 20l12 6 18-8"/><path d="M4 26l12 6 18-8"/></svg>Lightweight and suitable<br>for everyday use</div>
  <div class="feature" style="left:873px"><svg width="46" height="38" viewBox="0 0 46 38" fill="none" stroke="#fff" stroke-width="1.3"><path d="M6 26c-4-2-3-9 3-9 1-6 8-8 12-4 3-5 12-4 12 3 6-1 9 6 4 9l2 5-6-2-4 4-4-4-6 4-4-4-6 2z"/></svg>Handmade locally<br>in Switzerland</div>
</section>

<h2 class="abs display h-mid" style="left:147px;top:2603px">Story Creation</h2>
<p class="abs body-text" style="left:147px;top:2678px;width:345px">Each scarf begins with carefully selected fabrics. Colors, patterns and details are combined to create a unique piece.</p>
<div class="btn btn-sm" style="left:147px;top:2786px;width:137px;height:45px">Read More</div>
<div class="abs story-img" role="img" aria-label="Woman in a knit hat, sunglasses and scarf leaning on a brick wall"></div>

<section class="abs testi"></section>
<h2 class="abs display section-title" style="top:3008px;font-size:38px">Testimonials</h2>
<svg class="abs" style="left:571px;top:3083px" width="58" height="40" viewBox="0 0 58 40" fill="none" stroke="#222326" stroke-width="1.4"><circle cx="13" cy="13" r="11"/><path d="M24 13c0 14-8 22-16 24"/><circle cx="43" cy="13" r="11"/><path d="M54 13c0 14-8 22-16 24"/></svg>
<p class="abs section-title" style="top:3148px;font-size:18px;font-style:italic">My favorite scarf – I already own several.</p>
<p class="abs section-title" style="top:3196px;font-size:13px;font-weight:600">- LENA</p>
<div class="arrow" style="left:148px"><svg width="18" height="10" viewBox="0 0 18 10" fill="none" stroke="#222326" stroke-width="1.3"><path d="M17 5H1M5 1L1 5l4 4"/></svg></div>
<div class="arrow" style="left:1012px"><svg width="18" height="10" viewBox="0 0 18 10" fill="none" stroke="#222326" stroke-width="1.3"><path d="M1 5h16M13 1l4 4-4 4"/></svg></div>

<div class="abs everyday-img" role="img" aria-label="Woman with a bicycle on a city street wearing a warm scarf"></div>
<h2 class="abs display h-mid" style="left:734px;top:3388px">Everyday</h2>
<p class="abs body-text" style="left:734px;top:3463px;width:330px">Whether in everyday life, at the office or on a walk – KOR-VADO scarves bring color &amp; lightness to any outfit.</p>
<div class="btn btn-sm" style="left:734px;top:3573px;width:135px;height:43px">Read More</div>

<h2 class="abs display section-title" style="top:3734px;font-size:80px;line-height:100px">Discover Your Unique Scarf</h2>
<div class="btn btn-sm" style="left:500px;top:3877px;width:198px;height:42px">Discover Scarves</div>

<footer class="abs footer">
  <h2 class="abs display">Subscribe To Our News Letter</h2>
  <p class="abs lead">Find out when new models are released and where you can meet KOR-VADO in person. I also share tips on how to wear the scarves.</p>
  <div class="abs sub-form"><span>Enter Your Email Here</span><b>SUBSCRIBE</b></div>
  <div class="fcol" style="left:131px"><h3>Quick Links</h3>All Products<br>Triangular Scarves<br>Headscarves (New)<br>Small Triangular Scarf</div>
  <div class="fcol" style="left:378px"><h3>Other Links</h3>Seek<br>General Terms &amp; Conditions of Business<br>Data Protection<br>Imprint<br>Shipping Conditions<br>Refunds<br>Privacy Settings</div>
  <div class="fcol" style="left:753px"><h3>Contact Us</h3>
    <div style="padding-left:22px;position:relative"><svg style="position:absolute;left:0;top:6px" width="12" height="12" viewBox="0 0 12 12" fill="#fff"><path d="M2 1l3 0 1 3-2 1c1 2 2 3 3 3l1-2 3 1v3c-6 0-10-4-10-9z"/></svg><span class="lbl">PHONE NUMBER</span><span class="val">(08) 4417 2290</span></div>
    <div style="padding-left:22px;position:relative;margin-top:10px"><svg style="position:absolute;left:0;top:7px" width="12" height="9" viewBox="0 0 12 9" fill="#fff"><path d="M0 0h12v9H0z M1 1l5 4 5-4"/></svg><span class="lbl">EMAIL</span><span class="val">atelier@korvado-mail.ch</span></div>
    <div class="social"><i></i><i></i></div>
  </div>
  <div class="abs copyright">Copyright © 2026 KOR-VADO</div>
  <div class="abs pay"><i></i><i></i><i></i><i></i><i></i><i></i></div>
</footer>

</body>
</html>
```